Bramble Café retail envelop design

This is a single serve coffee product for the adventurer consumer. The product is Fair Trade, Organic coffee grounds in a single serve pouch that can be used as a quality pour over drip brew while on the go. We would like to use designs that show adventure/hiking/camping with earth tones that display a organic/biodegradable feel.The open width of envelope film is 200mmThe finished bag size is W 100mm * L 120mm. (Once sealed)The eye mark size is W 10* H 5 mm. (side seam)Top/Bottom heat seal: 8mmSide heat seal: 7mmPlease use the samples provided as a guide only. I would like to see what you can come up with. Please use our original logo attached.Three blend varieties: Kelvermoor, Hollow, WarsawIG: @Bramblecafe

Target Market(s)

Adventurers, backpackers, campers, hikers, adventure riders, etc.

Colors

Designer to choose colors to be used in the design.

Requirements
Must have
• My Bramble Cafe logo, earthy feel (maybe black logo on earthy paper color backdrop?). Must show 12g size, instruction panel (this can be edited for visual appeal), IG account: Bramblecafe.
• Design will be printed in Matte finish.
Should not have
• It does not need all of the text that is shown on the back. I will prefer a more simplistic design rather than a crowded one.

```html
<!DOCTYPE html>
<html lang="en">
<head>
<meta charset="utf-8">
<title>Bramble Café – Single Serve Pouch</title>
<link rel="stylesheet" href="https://fonts.googleapis.com/css2?family=Oswald:wght@500;600&family=Yellowtail&display=block">
<style>
  :root {
    --backdrop: #ffffff;
    --pouch-brown: #3b2116;
    --pouch-edge: #2e1910;
    --rust: #e2542a;
    --ink: #1a1210;
    --cream: #f4ece4;
    --sketch-mid: #6e5a4f;
    --sketch-light: #8a7a70;
  }
  * { margin: 0; padding: 0; box-sizing: border-box; }
  html, body {
    width: 1200px;
    height: 1190px;
    overflow: hidden;
    background: var(--backdrop);
  }
  .canvas {
    position: relative;
    width: 1200px;
    height: 1190px;
  }
  .pouch {
    position: absolute;
    left: 326px;
    top: 240px;
    width: 540px;
    height: 736px;
    background: var(--pouch-brown);
    border-radius: 10px 10px 4px 4px;
    overflow: hidden;
    box-shadow: inset 0 0 0 22px var(--pouch-edge);
  }
  .seal-line {
    position: absolute;
    left: 30px;
    right: 30px;
    top: 78px;
    height: 2px;
    background: rgba(0,0,0,0.22);
  }
  .brand-band {
    position: absolute;
    left: 169px;
    width: 202px;
    top: 0;
    height: 280px;
    background: var(--rust);
    border-radius: 0 0 101px 101px;
  }
  .brand-badge {
    position: absolute;
    left: 180px;
    top: 86px;
    width: 180px;
    height: 180px;
    border-radius: 50%;
    border: 4px solid var(--ink);
    background: var(--rust);
    display: flex;
    align-items: center;
    justify-content: center;
    text-align: center;
  }
  .brand-name {
    font-family: "Oswald", sans-serif;
    font-weight: 600;
    font-size: 28px;
    line-height: 1.3;
    letter-spacing: 1px;
    color: var(--ink);
    text-transform: uppercase;
    padding-top: 6px;
  }
  .tagline {
    position: absolute;
    left: 0;
    right: 0;
    top: 298px;
    text-align: center;
    font-family: "Yellowtail", cursive;
    font-size: 56px;
    color: var(--cream);
    line-height: 1;
  }
  .serve-label {
    position: absolute;
    left: 0;
    right: 0;
    top: 368px;
    text-align: center;
    font-family: "Oswald", sans-serif;
    font-weight: 500;
    font-size: 22px;
    letter-spacing: 1px;
    color: var(--cream);
    text-transform: uppercase;
  }
  .blend-name {
    position: absolute;
    left: 0;
    right: 0;
    top: 396px;
    text-align: center;
    font-family: "Yellowtail", cursive;
    font-weight: 400;
    font-size: 70px;
    color: var(--rust);
    line-height: 1.1;
  }
  .landscape {
    position: absolute;
    left: 22px;
    right: 22px;
    top: 484px;
    bottom: 14px;
    background:
      linear-gradient(180deg,
        rgba(138,122,112,0) 0%,
        rgba(138,122,112,0.45) 12%,
        rgba(110,90,79,0.25) 40%,
        rgba(110,90,79,0.05) 55%,
        rgba(138,122,112,0.5) 75%,
        rgba(138,122,112,0.55) 100%);
  }
  .net-weight {
    position: absolute;
    left: 470px;
    top: 656px;
    width: 62px;
    height: 62px;
    border-radius: 50%;
    background: var(--ink);
    border: 2px solid var(--cream);
    color: var(--cream);
    font-family: "Oswald", sans-serif;
    font-weight: 500;
    font-size: 26px;
    display: flex;
    align-items: center;
    justify-content: center;
  }
</style>
</head>
<body>
  <main class="canvas">
    <section class="pouch">
      <div class="seal-line"></div>
      <div class="brand-band"></div>
      <div class="brand-badge">
        <span class="brand-name">Bramble<br>Café</span>
      </div>
      <p class="tagline">Quality Roast</p>
      <p class="serve-label">Single Serve</p>
      <h1 class="blend-name">Kelvermoor</h1>
      <div class="landscape" role="img" aria-label="White line-drawn mountain range above a row of sketched pine trees along the bottom of the pouch"></div>
      <div class="net-weight">12g</div>
    </section>
  </main>
</body>
</html>
```